"Hot Streak Aunt" Comedy Tour needs show poster

I need a fun poster for my new comedy tour called "Hot Streak Aunt." This poster will be used by theaters and performing arts centers as well as on social media posts to promote the show.
Note: Please use 8.5"x11" dimensions for the poster. We would love vector images where possible in case the design needs to be scaled for social media.
Note: The poster will be used for different venues & dates, so you can put a lorem ipsum space for that somewhere on the poster.

Title Meaning:
If you do something "full send," you’re doing it it full-throttle and with 100% commitment—even if you end up failing - which can be funny. In extended, popular slang, full send has the sense of “intense,” “hardcore,” or “without regard to consequences.”
In terms of the comedy material in the show, I am a mom sending kids off to college and into the world. But I am also an athlete who does open water swimming, triathlons, snow skiing, etc. I think the poster would be funny showing a depiction of those activities (skiing, biking, or swimming) in a comical way.

It would be fun to have bright, retro colors & design elements from the 70s & 80s.
I am attaching some ski photos for that. "Full Send" or "Yard Sale" are both snow ski related too.
I am also attaching several photos/headshots that can be used in some way, but stylized (or just cut out the face part) as I am most interested in the graphics part of this poster. Maybe my face on a retro 80s skier body with bright colors?

Also, please note: I have always have great success here with very talented designers who know much more than me about the artwork. Please feel free to submit anything - I am open to suggestions and different interpretations. Thanks!!

Target Market(s)

Women ages 40+, Parents ages 30+, Couples ages 40+

Industry/Entity Type

Comedy, Entertainment

Requirements
Must have
• Tour Name (Hot Streak Aunt) & my name (Delia Fenwick)
Nice to have
• Would love to see a fun character in "Full Send" mode.
Should not have
• No trite references to motherhood (bottles, strollers, etc) or small children (my kids are grown). This poster is more about the fun and humor of "Full Send" in a comical way through skiiing, biking, or swimming .Please feel free to send questions!

```html
<!DOCTYPE html>
<html lang="en">
<head>
<meta charset="utf-8">
<title>Hot Streak Aunt – Comedy Tour Poster</title>
<link href="https://fonts.googleapis.com/css2?family=Orbitron:wght@700;900&family=Montserrat:wght@400&display=swap" rel="stylesheet">
<style>
  :root {
    --page: #ffffff;
    --ink: #000000;
    --white: #ffffff;
    --glow: #3cc8d2;
    --magenta: #c13aa8;
    --rose: #d2386e;
    --blue: #3f66d6;
    --aqua-shirt: #cdeef0;
    --hair: #d9bf99;
  }
  html, body {
    margin: 0;
    width: 814px;
    height: 1200px;
    overflow: hidden;
    background: var(--page);
  }
  .poster {
    position: absolute;
    left: 22px;
    top: 26px;
    width: 769px;
    height: 1155px;
    background: var(--ink);
    overflow: hidden;
    font-family: "Orbitron", sans-serif;
    color: var(--white);
  }
  .side-glow {
    position: absolute;
    top: 180px;
    width: 70px;
    height: 520px;
    filter: blur(14px);
  }
  .side-glow--left {
    left: -30px;
    background: linear-gradient(180deg, transparent 0%, var(--magenta) 30%, var(--blue) 70%, transparent 100%);
  }
  .side-glow--right {
    right: -30px;
    background: linear-gradient(180deg, transparent 0%, var(--rose) 35%, var(--blue) 72%, transparent 100%);
  }
  .center-glow {
    position: absolute;
    left: 170px;
    top: 600px;
    width: 440px;
    height: 260px;
    border-radius: 50%;
    background: radial-gradient(ellipse at center, rgba(190,40,90,0.75) 0%, rgba(80,30,120,0.45) 40%, transparent 72%);
    filter: blur(10px);
  }
  .sparkles {
    position: absolute;
    inset: 0;
  }
  .headshot {
    position: absolute;
    left: 200px;
    top: 93px;
    width: 412px;
    height: 510px;
    border-radius: 150px 150px 20px 20px;
    background:
      radial-gradient(ellipse 34% 30% at 48% 28%, var(--hair) 0%, rgba(217,191,153,0.8) 60%, transparent 100%),
      linear-gradient(180deg, rgba(217,191,153,0.6) 0%, var(--aqua-shirt) 55%, #bfe4e7 100%);
  }
  .title {
    position: absolute;
    left: 0;
    width: 100%;
    text-align: center;
    font-weight: 900;
    font-style: italic;
    transform: skewX(-8deg);
    text-shadow: 0 0 6px var(--glow), 0 0 16px var(--glow), 0 0 28px rgba(60,200,210,0.6);
    margin: 0;
    line-height: 1;
  }
  .title--top { top: 548px; font-size: 62px; letter-spacing: 1px; }
  .title--main { top: 618px; font-size: 128px; letter-spacing: 2px; }
  .tour-line {
    position: absolute;
    left: 0;
    width: 100%;
    text-align: center;
    font-weight: 900;
    line-height: 1;
    margin: 0;
    text-shadow: 0 0 8px rgba(60,200,210,0.7);
  }
  .tour-line--tour { top: 792px; font-size: 37px; }
  .tour-line--with { top: 838px; font-size: 40px; }
  .performer {
    position: absolute;
    left: 178px;
    top: 904px;
    width: 451px;
    height: 41px;
    border: 3px solid var(--white);
    box-shadow: 0 0 8px var(--glow), inset 0 0 8px var(--glow);
    display: flex;
    align-items: center;
    justify-content: center;
    font-weight: 900;
    font-size: 22px;
    letter-spacing: 12px;
    padding-left: 12px;
    box-sizing: border-box;
    text-shadow: 0 0 6px var(--glow);
  }
  .details {
    position: absolute;
    left: 0;
    top: 992px;
    width: 100%;
    text-align: center;
    font-weight: 900;
    font-size: 18.5px;
    text-shadow: 0 0 6px var(--glow);
    margin: 0;
  }
  .venue-info {
    position: absolute;
    left: 0;
    top: 1040px;
    width: 100%;
    text-align: center;
    font-family: "Montserrat", sans-serif;
    font-size: 15px;
    line-height: 1.3;
    margin: 0;
  }
</style>
</head>
<body>
  <main class="poster">
    <div class="side-glow side-glow--left"></div>
    <div class="side-glow side-glow--right"></div>
    <div class="center-glow"></div>
    <svg class="sparkles" width="769" height="1155" aria-hidden="true">
      <g fill="#ffffff" opacity="0.8">
        <circle cx="70" cy="975" r="2.5"/><circle cx="110" cy="930" r="1.5"/>
        <circle cx="95" cy="870" r="2"/><circle cx="140" cy="1010" r="1.5"/>
        <circle cx="190" cy="880" r="1.2"/><circle cx="660" cy="930" r="2"/>
        <circle cx="700" cy="870" r="1.5"/><circle cx="690" cy="1000" r="1.2"/>
        <circle cx="640" cy="830" r="1.5"/><circle cx="730" cy="800" r="1.5"/>
        <circle cx="45" cy="780" r="1.5"/><circle cx="580" cy="790" r="1.2"/>
        <circle cx="360" cy="760" r="2"/><circle cx="650" cy="650" r="2"/>
      </g>
    </svg>
    <div class="headshot" role="img" aria-label="Cut-out headshot of the comedian, smiling, in a pale aqua quarter-zip top"></div>
    <h1 class="title title--top">HOT STREAK</h1>
    <h1 class="title title--main">AUNT</h1>
    <p class="tour-line tour-line--tour">COMDEY TOUR</p>
    <p class="tour-line tour-line--with">WITH</p>
    <div class="performer">DELIA FENWICK</div>
    <p class="details">ENTRY $15 // ALL NIGHT // FREE PARKING</p>
    <p class="venue-info">Lorem ipsum dolor sit amet, consectetuer adipiscing elit, sed<br>diam nonummy nibh euismod.</p>
  </main>
</body>
</html>
```